Hello Creative Minds!
Our business is after a elegant and classy flyer that draws attention!
The business is Velmora Turf - Lawn Rejuvenation Services. We provide services that maintain a healthy and vibrant green lawn through the tough Australian seasons. The products we use limits the water needed to keep grass green to a minimum - practically none at all! This not only helps the home owner or home seller but the environment by limiting the use of water that is needed to create a green lawn. The products we use are made from natural ingredients that are and pet friendly.
This fly will be our introductory offer to the market. Below are the required points that need to be on the flyer. Attached is the business logo, before & after pictures and 1 example of the LAYOUT not DESIGN of what the flyer should be laid out like or similar to. Feel free to use different 'Lawn Mower' pictures.
All the best; if you need any questions answered please feel free to message.
REQUIRED POINTS (Please re-phrase were possible);
*Instantly restores the natural green colour of grass – year round
*Lasts for up to 3 months
*Substantially reduces watering needs
*Pet friendly
*Stays green during droughts and water restrictions
*UV fade resistant
*Won’t bleed, run, or stain once absorbed into the grass
*Safe for the environment, pets and people
*Works in extreme heat, cold and frost
*Organic and natural – no harmful chemicals
*Reduces the amount of fertilizer
and water used on lawns
*Kerb appeal is essential for getting your property sold for the highest price possible
SERVICES & PRICING
Lawn maintenance (cut & trim) starting from $60
Lawn rejuvenation starting from $80 (Only $27 a month for 3 months)*
Package deal starting from $120
Introductory offer: 25% off all services. Refer a friend, when they book you receive another 25% off your next service.
LOCATIONS
Nowra to Sydney
CONTACT NUMBER
Will be posted with the winner - please leave an area for this.
SOCIAL MEDIA
Please add Chatterloop and Snapvista logo's
Updates
Competition has finished, thank you to all that have participated! I will review and comment on the flyers that need assistance. All the best with future designs!
Target Market(s)
home owners, home sellers, property developers, real estates and nursing homes and government housing.
Industry/Entity Type
Lawn Care
Look and feel
Each slider illustrates characteristics of the customer's brand and the style your logo design should communicate.

```html
<!DOCTYPE html>
<html lang="en">
<head>
<meta charset="utf-8">
<title>Velmora Turf - Lawn Rejuvenation Services</title>
<link rel="stylesheet" href="https://fonts.googleapis.com/css2?family=Open+Sans:wght@400;600;700;800&display=swap">
<style>
  :root {
    --page-bg: #e9e9e7;
    --green-deep: #2c6a1c;
    --green-mid: #4f9a27;
    --green-light: #8cc63f;
    --green-pale: #b9dc7e;
    --pill-green: #7dbb35;
    --white: #ffffff;
    --ink: #3a3a3a;
    --ring: rgba(255,255,255,0.75);
  }
  * { margin: 0; padding: 0; box-sizing: border-box; }
  html, body { width: 954px; height: 1200px; overflow: hidden; }
  body { background: var(--page-bg); font-family: "Open Sans", Arial, sans-serif; position: relative; }

  .flyer { position: absolute; left: 57px; top: 5px; width: 840px; height: 1190px; overflow: hidden; background: var(--green-deep); }
  .flyer-shapes { position: absolute; inset: 0; }

  .brand { position: absolute; left: 40px; top: 418px; width: 360px; color: var(--ink); text-align: center; }
  .brand-name { font-size: 54px; font-weight: 600; letter-spacing: 1px; line-height: 1; }
  .brand-tagline { font-size: 12px; font-weight: 600; letter-spacing: 5px; margin-top: 14px; }

  .services-pill { position: absolute; left: 28px; top: 596px; width: 216px; height: 36px; border-radius: 18px;
    background: var(--pill-green); color: var(--white); font-weight: 800; font-size: 19px; line-height: 36px; padding-left: 18px; letter-spacing: .5px; }

  .benefits { position: absolute; left: 36px; top: 652px; width: 500px; list-style: none; color: var(--white); }
  .benefits li { position: relative; padding-left: 30px; font-size: 16.5px; font-weight: 700; line-height: 22px; margin-bottom: 7px; }
  .benefits li svg { position: absolute; left: 0; top: 2px; width: 18px; height: 18px; }
  .benefits li.plain { padding-left: 30px; }

  .price-box { position: absolute; left: 568px; width: 236px; border: 2px dashed var(--white); border-radius: 12px;
    color: var(--white); text-align: center; font-weight: 700; display: flex; flex-direction: column; justify-content: center; }
  .price-box .title { font-size: 17px; font-weight: 800; }
  .price-box .detail { font-size: 16px; }
  .price-box .note { font-size: 11px; font-weight: 600; }
  .price-box .offer-label { font-size: 12px; font-weight: 600; }
  .price-box .offer { font-size: 19px; font-weight: 800; }
  .price-box .fine { font-size: 9.5px; font-weight: 600; line-height: 12px; padding: 0 12px; margin-top: 3px; }
  .box-maintenance { top: 644px; height: 100px; }
  .box-rejuvenation { top: 760px; height: 96px; }
  .box-package { top: 870px; height: 94px; }
  .box-intro { top: 980px; height: 94px; }

  .estimate-pill { position: absolute; left: 164px; top: 1104px; width: 530px; height: 44px; border-radius: 22px;
    background: var(--white); color: var(--green-mid); font-weight: 800; font-size: 24px;
    display: flex; align-items: center; justify-content: center; gap: 12px; }
  .estimate-pill svg { width: 26px; height: 26px; }
  .website { position: absolute; left: 164px; top: 1152px; width: 530px; text-align: center; color: var(--white); font-weight: 800; font-size: 20px; }

  .social { position: absolute; left: 30px; top: 1116px; display: flex; flex-direction: column; gap: 6px; }
  .social-item { display: flex; align-items: center; gap: 6px; color: var(--white); font-size: 12px; font-weight: 700; }
  .social-item .dot { width: 18px; height: 18px; border-radius: 50%; background: var(--white); }
</style>
</head>
<body>
<main class="flyer">
  <svg class="flyer-shapes" viewBox="0 0 840 1190" width="840" height="1190">
    <defs>
      <linearGradient id="greenBase" x1="0" y1="0" x2="0" y2="1">
        <stop offset="0" stop-color="#2c6a1c"/>
        <stop offset="0.55" stop-color="#3f8a22"/>
        <stop offset="0.85" stop-color="#6fb332"/>
        <stop offset="1" stop-color="#8cc63f"/>
      </linearGradient>
      <linearGradient id="houseTones" x1="0" y1="0" x2="0" y2="1">
        <stop offset="0" stop-color="#c9ccc6"/>
        <stop offset="0.5" stop-color="#8e9a86"/>
        <stop offset="1" stop-color="#5e9b34"/>
      </linearGradient>
      <linearGradient id="grassStrip" x1="0" y1="0" x2="0" y2="1">
        <stop offset="0" stop-color="#8cc63f" stop-opacity="0"/>
        <stop offset="0.4" stop-color="#a6d35c"/>
        <stop offset="1" stop-color="#6fae30"/>
      </linearGradient>
      <linearGradient id="beforeAfter" x1="0" y1="0" x2="1" y2="0">
        <stop offset="0.5" stop-color="#b6a77a"/>
        <stop offset="0.5" stop-color="#6aa640"/>
      </linearGradient>
    </defs>

    <rect x="0" y="0" width="840" height="450" fill="url(#houseTones)" role="img" aria-label="Photo of a suburban house with a lush green front lawn"/>

    <path d="M0,395 C200,350 500,330 840,330 L840,1190 L0,1190 Z" fill="url(#greenBase)"/>
    <path d="M0,410 C180,370 420,380 620,430 L620,520 C430,520 200,520 0,570 Z" fill="var(--white)"/>

    <rect x="0" y="1040" width="840" height="150" fill="url(#grassStrip)" role="img" aria-label="Photo of fresh green grass blades along the bottom edge"/>

    <circle cx="130" cy="310" r="78" fill="#7fbf45" stroke="#d9dcd6" stroke-width="8" role="img" aria-label="Hand holding a magnifying glass over green grass"/>

    <circle cx="642" cy="384" r="142" fill="var(--ring)"/>
    <circle cx="642" cy="384" r="130" fill="url(#beforeAfter)" role="img" aria-label="Before and after photo of a driveway lawn, dry on the left and green on the right"/>
    <text x="580" y="320" font-family="Open Sans, sans-serif" font-size="16" font-style="italic" fill="#ffffff">before</text>
    <text x="668" y="320" font-family="Open Sans, sans-serif" font-size="16" font-style="italic" fill="#ffffff">after</text>

    <circle cx="516" cy="526" r="100" fill="var(--ring)"/>
    <circle cx="516" cy="526" r="88" fill="#b89c68" role="img" aria-label="Close-up photo of dry patchy lawn turning green"/>

    <circle cx="730" cy="516" r="100" fill="var(--ring)"/>
    <circle cx="730" cy="516" r="88" fill="#5f9f38" role="img" aria-label="Photo of a lawn mower cutting green grass"/>
  </svg>

  <div class="brand">
    <div class="brand-name">Velmora Turf</div>
    <div class="brand-tagline">LAWN REJUVENATION SERVICES</div>
  </div>

  <div class="services-pill">OUR SERVICES</div>

  <ul class="benefits">
    <li><svg viewBox="0 0 18 18"><circle cx="9" cy="9" r="9" fill="#fff"/><path d="M5 9.3l2.7 2.7L13 6.6" stroke="#3f8a22" stroke-width="2.2" fill="none"/></svg>Instantly restores the natural green colour of<br>grass – year round</li>
    <li><svg viewBox="0 0 18 18"><circle cx="9" cy="9" r="9" fill="#fff"/><path d="M5 9.3l2.7 2.7L13 6.6" stroke="#3f8a22" stroke-width="2.2" fill="none"/></svg>Lasts for up to 3 months</li>
    <li><svg viewBox="0 0 18 18"><circle cx="9" cy="9" r="9" fill="#fff"/><path d="M5 9.3l2.7 2.7L13 6.6" stroke="#3f8a22" stroke-width="2.2" fill="none"/></svg>Substantially reduces watering needs</li>
    <li><svg viewBox="0 0 18 18"><circle cx="9" cy="9" r="9" fill="#fff"/><path d="M5 9.3l2.7 2.7L13 6.6" stroke="#3f8a22" stroke-width="2.2" fill="none"/></svg>Pet friendly</li>
    <li><svg viewBox="0 0 18 18"><circle cx="9" cy="9" r="9" fill="#fff"/><path d="M5 9.3l2.7 2.7L13 6.6" stroke="#3f8a22" stroke-width="2.2" fill="none"/></svg>Stays green during droughts and water restrictions</li>
    <li><svg viewBox="0 0 18 18"><circle cx="9" cy="9" r="9" fill="#fff"/><path d="M5 9.3l2.7 2.7L13 6.6" stroke="#3f8a22" stroke-width="2.2" fill="none"/></svg>UV fade resistant</li>
    <li><svg viewBox="0 0 18 18"><circle cx="9" cy="9" r="9" fill="#fff"/><path d="M5 9.3l2.7 2.7L13 6.6" stroke="#3f8a22" stroke-width="2.2" fill="none"/></svg>Won’t bleed, run, or stain once absorbed into<br>the grass</li>
    <li><svg viewBox="0 0 18 18"><circle cx="9" cy="9" r="9" fill="#fff"/><path d="M5 9.3l2.7 2.7L13 6.6" stroke="#3f8a22" stroke-width="2.2" fill="none"/></svg>Safe for the environment, pets and people</li>
    <li class="plain">Works in extreme heat, cold and frost</li>
    <li><svg viewBox="0 0 18 18"><circle cx="9" cy="9" r="9" fill="#fff"/><path d="M5 9.3l2.7 2.7L13 6.6" stroke="#3f8a22" stroke-width="2.2" fill="none"/></svg>Organic and natural – no harmful chemicals</li>
    <li><svg viewBox="0 0 18 18"><circle cx="9" cy="9" r="9" fill="#fff"/><path d="M5 9.3l2.7 2.7L13 6.6" stroke="#3f8a22" stroke-width="2.2" fill="none"/></svg>Reduces the amount of fertilizer<br>and water used on lawns</li>
    <li><svg viewBox="0 0 18 18"><circle cx="9" cy="9" r="9" fill="#fff"/><path d="M5 9.3l2.7 2.7L13 6.6" stroke="#3f8a22" stroke-width="2.2" fill="none"/></svg>Kerb appeal is essential for getting your property<br>sold for the highest price possible</li>
  </ul>

  <div class="price-box box-maintenance">
    <div class="title">LAWN MAINTENANCE</div>
    <div class="detail">(cut &amp; trim)</div>
    <div class="detail">starting from $60</div>
  </div>
  <div class="price-box box-rejuvenation">
    <div class="title">LAWN REJUVENATION</div>
    <div class="detail">starting from $80</div>
    <div class="note">(Only $27 a month for 3 months)*</div>
  </div>
  <div class="price-box box-package">
    <div class="title">PACKAGE DEAL</div>
    <div class="detail">starting from $120</div>
  </div>
  <div class="price-box box-intro">
    <div class="offer-label">INTRODUCTORY OFFER:</div>
    <div class="offer">25% off all services</div>
    <div class="fine">Refer a friend, when they book you receive another 25% off your next service.</div>
  </div>

  <div class="social">
    <div class="social-item"><span class="dot"></span>Chatterloop</div>
    <div class="social-item"><span class="dot"></span>Snapvista</div>
  </div>

  <div class="estimate-pill">
    <span>FREE ESTIMATE</span>
    <svg viewBox="0 0 26 26"><circle cx="13" cy="13" r="11.5" fill="none" stroke="#4f9a27" stroke-width="2"/><path d="M9 7.5l2.2-.6 1.4 3-1.5 1.2c.7 1.6 1.8 2.7 3.4 3.4l1.2-1.5 3 1.4-.6 2.2c-5 .4-9.5-4.1-9.1-9.1z" fill="#4f9a27"/></svg>
    <span>555 010 4821</span>
  </div>
  <div class="website">www.VelmoraTurf.com</div>
</main>
</body>
</html>
```